Create a professional, eye-catching business card design that reflects the values and services of Brookfern Veterinary Hospital. we provide veterinary services and the business card should be a memorable representation of the clinic and align with its branding and mission. our tag line is "Life Long Companions, Lifelong Care"
Use clean, modern typography. Prioritize readability and professionalism. We would like to see designs that use the color blue, as in the logo example. the final design should communicate professionalism and care, with attention to detail.

```html
<!DOCTYPE html>
<html lang="en">
<head>
<meta charset="utf-8">
<title>Brookfern Veterinary Hospital – Business Card</title>
<link href="https://fonts.googleapis.com/css2?family=Montserrat:wght@500;600;700;800&display=swap" rel="stylesheet">
<style>
  :root {
    --navy: #1f3161;
    --ink: #1f2f5e;
    --paper: #ffffff;
    --backdrop: #8a8a8a;
  }
  * { box-sizing: border-box; margin: 0; padding: 0; }
  html, body { width: 976px; height: 1200px; overflow: hidden; }
  body {
    background: var(--backdrop);
    font-family: "Montserrat", Arial, sans-serif;
    color: var(--ink);
    position: relative;
  }
  .card {
    position: absolute;
    left: 91px;
    width: 793px;
    height: 453px;
    background: var(--paper);
    overflow: hidden;
  }
  .card--front { top: 91px; }
  .card--back { top: 655px; }
  .card__corners {
    position: absolute;
    inset: 0;
    width: 100%;
    height: 100%;
  }
  .card__corners path { fill: var(--navy); }

  .brand {
    position: absolute;
    display: flex;
    flex-direction: column;
    align-items: center;
    color: var(--navy);
    font-weight: 800;
    text-transform: uppercase;
    line-height: 1;
  }
  .brand__mark {
    width: 150px;
    height: 150px;
    border: 2px solid var(--navy);
    border-radius: 50%;
    margin-bottom: 16px;
  }
  .brand__name { font-size: 44px; letter-spacing: 0.5px; }
  .brand__sub { font-size: 15.5px; margin-top: 6px; letter-spacing: 0.3px; }
  .card--front .brand { left: 0; right: 0; top: 120px; }
  .card--back .brand { left: 474px; width: 240px; top: 135px; }
  .card--back .brand__mark { width: 140px; height: 140px; margin-bottom: 14px; }
  .card--back .brand__name { font-size: 39px; }
  .card--back .brand__sub { font-size: 13.7px; }

  .holder {
    position: absolute;
    left: 64px;
    top: 68px;
  }
  .holder__name {
    font-size: 42px;
    font-weight: 800;
    color: var(--navy);
    line-height: 1;
    letter-spacing: 0.3px;
  }
  .holder__role {
    font-size: 15px;
    font-weight: 600;
    letter-spacing: 2.6px;
    margin-top: 10px;
    text-transform: uppercase;
  }
  .holder__rule {
    width: 190px;
    height: 2px;
    background: var(--navy);
    margin-top: 16px;
  }
  .contacts {
    position: absolute;
    left: 70px;
    top: 206px;
    list-style: none;
  }
  .contact {
    display: flex;
    align-items: center;
    height: 28px;
    margin-bottom: 34px;
    font-size: 18px;
    font-weight: 600;
  }
  .contact__icon {
    width: 28px;
    height: 28px;
    margin-right: 19px;
    flex: none;
  }
</style>
</head>
<body>

  <section class="card card--front" aria-label="Card front">
    <svg class="card__corners" viewBox="0 0 1050 600" preserveAspectRatio="none" aria-hidden="true">
      <path d="M729 0 C900 0 1040 150 1050 360 L1050 0 Z"/>
      <path d="M0 290 C10 480 150 600 330 600 L0 600 Z"/>
    </svg>
    <div class="brand">
      <div class="brand__mark"></div>
      <div class="brand__name">Brookfern</div>
      <div class="brand__sub">Veterinary Hospital</div>
    </div>
  </section>

  <section class="card card--back" aria-label="Card back">
    <svg class="card__corners" viewBox="0 0 1050 600" preserveAspectRatio="none" aria-hidden="true">
      <path d="M729 0 C900 0 1040 150 1050 360 L1050 0 Z"/>
      <path d="M0 290 C10 480 150 600 330 600 L0 600 Z"/>
    </svg>

    <div class="holder">
      <div class="holder__name">BROOKFERN</div>
      <div class="holder__role">Designation</div>
      <div class="holder__rule"></div>
    </div>

    <ul class="contacts">
      <li class="contact">
        <svg class="contact__icon" viewBox="0 0 28 28" aria-hidden="true">
          <circle cx="14" cy="14" r="14" fill="var(--navy)"/>
          <path d="M10.2 7.5c.6-.3 1.2 0 1.5.5l1.2 2.3c.3.6.1 1.2-.4 1.5l-.8.5c.6 1.6 1.9 2.9 3.5 3.6l.5-.8c.3-.5 1-.7 1.5-.4l2.3 1.2c.5.3.8.9.5 1.5-.5 1.5-1.8 2.3-3.1 2-4.2-.9-7.3-4-8.2-8.2-.3-1.3.5-2.7 1.5-3.2z" fill="#fff"/>
        </svg>
        +070 4182 39507
      </li>
      <li class="contact">
        <svg class="contact__icon" viewBox="0 0 28 28" aria-hidden="true">
          <circle cx="14" cy="14" r="14" fill="var(--navy)"/>
          <rect x="7.5" y="9.5" width="13" height="9" rx="1" fill="none" stroke="#fff" stroke-width="1.6"/>
          <path d="M7.8 10l6.2 5 6.2-5M7.8 18l4.4-4M20.2 18l-4.4-4" fill="none" stroke="#fff" stroke-width="1.4"/>
        </svg>
        hello@brookfernvet.com
      </li>
      <li class="contact">
        <svg class="contact__icon" viewBox="0 0 28 28" aria-hidden="true">
          <circle cx="14" cy="14" r="14" fill="var(--navy)"/>
          <g fill="none" stroke="#fff" stroke-width="1.4">
            <circle cx="14" cy="14" r="7"/>
            <ellipse cx="14" cy="14" rx="3" ry="7"/>
            <path d="M7 14h14M8 10.5h12M8 17.5h12"/>
          </g>
        </svg>
        www.brookfernvet.com
      </li>
    </ul>

    <div class="brand">
      <div class="brand__mark"></div>
      <div class="brand__name">Brookfern</div>
      <div class="brand__sub">Veterinary Hospital</div>
    </div>
  </section>

</body>
</html>
```